Etiketten für Schaps
Zielgruppe
Erzeugung hochwertiger Spirituosen wie Vodka, Gin, Liköre, Schnäpse. Das Produktporfolio reicht vom klassischem Vodka bis zu Absinth oder Kräuterbitter. Finden Sie unsere Produkte unter: www.brunecker-destille.at
Zielgruppe: Export nach Asien bzw. Afrika an die immer größer werdende Bevölkerungsschicht, die europäische Qualität schätzt. Fokus auf das österr. Image: K. u. K Zeit, BERGFALKE, Sissy, Tradition, Kultur
Gesucht wird ein klassisches Spirituosenetikett
Aufgabenstellung
Gestaltung eines Vorderetiketts für eine eckige Flasche mit schwarzer Kapsel mit goldenem Aufdruck.
Verwendung des Logos 'B - Bergfalke ' (siehe Anlage), es soll jedoch neben Vodka und Gin auch eine Schnapsserie entwickelt werden: Sorten: Himbeergeist, Marillenschnaps, Williams-Christ-Birnenschnaos, Obstschnaps, Haselnuss-Schnaps
Größe des Etiketts: konisch, Breite oben: 53mm, Breite unten: 40 mll, Länge: max 150 mm, Ränder gewölbt, siehe
Stanze (siehe Anlage).
Die Farbe sollte in den Farben Gold/Schwarz gehalten werden, ev. auch eine rot-weiß-rote Fahne o.ä. als Hinweis auf die Herkunft
Ev. auch mit Fruchtabbildungen, diese können auch aus kommerziellen Bilddatenbanken genommen werden.

```html
<!DOCTYPE html>
<html lang="de">
<head>
<meta charset="utf-8">
<title>Bergfalke Himbeergeist – Etikettenserie</title>
<link rel="stylesheet" href="https://fonts.googleapis.com/css2?family=Cormorant+Garamond:wght@600&family=Open+Sans:wght@500&family=Pinyon+Script&display=swap">
<style>
  :root {
    --paper: #ffffff;
    --label-black: #000000;
    --damask-edge: #0c0c0c;
    --damask-mid: #1a1a1a;
    --gold-light: #f2dc8a;
    --gold: #c9a54a;
    --gold-dark: #8a6a22;
    --outline: #9a9a9a;
    --flag-red: #b0283a;
    --flag-white: #ffffff;
  }
  html, body {
    margin: 0;
    padding: 0;
    width: 1200px;
    height: 1141px;
    overflow: hidden;
    background: var(--paper);
  }
  .sheet { display: block; width: 1200px; height: 1141px; }
  .die-line { stroke: var(--outline); stroke-width: 1; }
  .label-body { fill: var(--label-black); }
  .damask-band { fill: url(#damaskTone); }
  .ornament { fill: url(#goldGlow); }
  .brand-frame { fill: var(--label-black); stroke: url(#goldFlat); }
  .brand-name {
    font-family: "Open Sans", sans-serif;
    font-weight: 500;
    fill: var(--gold);
    text-anchor: middle;
  }
  .variety-banner { fill: var(--label-black); stroke: var(--gold); stroke-width: 2.5; }
  .variety-name {
    font-family: "Cormorant Garamond", serif;
    font-weight: 600;
    font-size: 23px;
    letter-spacing: 2.5px;
    fill: var(--gold-light);
  }
  .premium {
    font-family: "Pinyon Script", cursive;
    fill: var(--gold);
    text-anchor: middle;
  }
  .fruit { fill: url(#berry); }
  .flag-red { fill: var(--flag-red); }
  .flag-white { fill: var(--flag-white); }
</style>
</head>
<body>
<svg class="sheet" viewBox="0 0 1200 1141" xmlns="http://www.w3.org/2000/svg">
  <defs>
    <linearGradient id="goldFlat" x1="0" y1="0" x2="1" y2="1">
      <stop offset="0" stop-color="#f2dc8a"/>
      <stop offset=".5" stop-color="#c9a54a"/>
      <stop offset="1" stop-color="#8a6a22"/>
    </linearGradient>
    <radialGradient id="goldGlow" cx=".5" cy=".5" r=".5">
      <stop offset="0" stop-color="#e0c26a" stop-opacity=".75"/>
      <stop offset=".55" stop-color="#b8933e" stop-opacity=".35"/>
      <stop offset="1" stop-color="#8a6a22" stop-opacity="0"/>
    </radialGradient>
    <linearGradient id="damaskTone" x1="0" y1="0" x2="1" y2="0">
      <stop offset="0" stop-color="#0c0c0c"/>
      <stop offset=".5" stop-color="#1a1a1a"/>
      <stop offset="1" stop-color="#0c0c0c"/>
    </linearGradient>
    <radialGradient id="berry" cx=".4" cy=".45" r=".6">
      <stop offset="0" stop-color="#d9477a"/>
      <stop offset=".7" stop-color="#b22a58"/>
      <stop offset="1" stop-color="#7a2a3a" stop-opacity="0"/>
    </radialGradient>
    <clipPath id="capClip"><circle cx="574" cy="380" r="100"/></clipPath>
    <path id="bannerArc" d="M152,662 Q236,632 322,662"/>
  </defs>

  <g class="front-label">
    <path class="label-body die-line" d="M66,200 C66,142 140,122 237,122 C340,122 407,140 407,195 L356,1073 L117,1073 Z"/>
    <rect class="damask-band" x="159" y="285" width="155" height="618" role="img" aria-label="Dunkles Damastmuster"/>
    <ellipse class="ornament" cx="237" cy="246" rx="130" ry="42" role="img" aria-label="Goldenes Barockornament oben"/>

    <ellipse class="brand-frame" cx="236" cy="494" rx="99" ry="132" stroke-width="4"/>
    <ellipse class="brand-frame" cx="236" cy="494" rx="70" ry="98" stroke-width="1.5"/>
    <text class="brand-name" x="236" y="503" font-size="22">BERGFALKE</text>

    <path class="variety-banner" d="M145,640 Q236,612 328,640 L328,678 Q236,652 145,678 Z"/>
    <text class="variety-name"><textPath href="#bannerArc" startOffset="50%" text-anchor="middle">Himbeergeist</textPath></text>

    <text class="premium" x="237" y="718" font-size="36">Premium</text>

    <ellipse class="fruit" cx="242" cy="795" rx="38" ry="42" role="img" aria-label="Himbeere mit Blättern"/>

    <ellipse class="ornament" cx="237" cy="922" rx="115" ry="38" role="img" aria-label="Goldenes Barockornament unten"/>

    <ellipse class="ornament" cx="191" cy="1019" rx="25" ry="15" role="img" aria-label="Kleines Goldornament links"/>
    <rect class="flag-white" x="219" y="1005" width="36" height="27"/>
    <rect class="flag-red" x="221" y="1007" width="32" height="7.5"/>
    <rect class="flag-red" x="221" y="1022.5" width="32" height="7.5"/>
    <ellipse class="ornament" cx="284" cy="1019" rx="25" ry="15" role="img" aria-label="Kleines Goldornament rechts"/>
  </g>

  <g class="cap-label">
    <circle class="label-body die-line" cx="574" cy="380" r="100"/>
    <rect class="damask-band" x="497" y="280" width="156" height="200" clip-path="url(#capClip)" role="img" aria-label="Dunkles Damastmuster"/>
    <ellipse class="brand-frame" cx="574" cy="381" rx="50" ry="72" stroke-width="3"/>
    <text class="brand-name" x="574" y="386" font-size="12">BERGFALKE</text>
  </g>

  <g class="capsule-wrap">
    <rect class="label-body die-line" x="472" y="500" width="635" height="381"/>
    <rect class="damask-band" x="503" y="501" width="156" height="379" role="img" aria-label="Dunkles Damastmuster"/>
    <rect class="damask-band" x="712" y="501" width="156" height="379" role="img" aria-label="Dunkles Damastmuster"/>
    <rect class="damask-band" x="921" y="501" width="156" height="379" role="img" aria-label="Dunkles Damastmuster"/>

    <ellipse class="brand-frame" cx="580" cy="738" rx="50" ry="72" stroke-width="3"/>
    <text class="brand-name" x="580" y="743" font-size="12">BERGFALKE</text>
    <text class="premium" x="580" y="846" font-size="34">Premium</text>

    <ellipse class="brand-frame" cx="791" cy="738" rx="50" ry="72" stroke-width="3"/>
    <text class="brand-name" x="791" y="743" font-size="12">BERGFALKE</text>
    <text class="premium" x="789" y="846" font-size="34">Premium</text>

    <ellipse class="brand-frame" cx="1000" cy="738" rx="50" ry="72" stroke-width="3"/>
    <text class="brand-name" x="1000" y="743" font-size="12">BERGFALKE</text>
    <text class="premium" x="998" y="846" font-size="34">Premium</text>
  </g>
</svg>
</body>
</html>
```